Deck Construction Company Billboard Design needed

We are a deck company with a 10'x32' billboard to fill with an advertisement. I'd like this ad to be 75% photo, 25% color-filled background with white text over (space to be divided side-to-side with line of some sort). This billboard artwork must be clearly legible and simple. The information I need on the billboard is as follows:
Plank QR (company name)
plankqr.ca
Outdoor Living Spaces
416-283-9061
Attached is a copy of the logo and photos I'd like to use (please choose one photo per billboard design)

Target Market(s)

30-70 year old home owners

Industry/Entity Type

Deck Builder

Font styles to use
Other font styles liked:
• Calibri

Colors
0054AA
0677BA
7BADD7
CADEEF
E8F1F8

Requirements
Must have
• Clear, simple white text. Dark blue fill, red accent
Nice to have
• Layering of photo and text
Should not have
• Too much to read

```html
<!DOCTYPE html>
<html lang="en">
<head>
<meta charset="UTF-8">
<title>Plank QR – Outdoor Living Spaces Billboard</title>
<link href="https://fonts.googleapis.com/css2?family=Montserrat:wght@700;800&family=Open+Sans:wght@600;700&display=swap" rel="stylesheet">
<style>
  :root {
    --navy: #1a1f52;
    --red: #e31b23;
    --white: #ffffff;
    --page: #eef1f4;
    --photo-green: #5f7f45;
    --photo-deck: #b9bcbf;
    --photo-pool: #3f8fb0;
  }
  * { margin: 0; padding: 0; box-sizing: border-box; }
  html, body {
    width: 1200px;
    height: 1000px;
    overflow: hidden;
    background: var(--page);
  }
  .billboard {
    position: absolute;
    left: 40px;
    top: 300px;
    width: 1120px;
    height: 400px;
    overflow: hidden;
    background: var(--navy);
  }
  .billboard-shapes {
    position: absolute;
    inset: 0;
  }
  .deck-photo {
    position: absolute;
    inset: 0;
    clip-path: polygon(640px 0, 1120px 0, 1120px 400px, 520px 400px);
    background:
      linear-gradient(180deg, rgba(95,127,69,0.95) 0%, rgba(95,127,69,0.7) 28%, rgba(63,143,176,0.55) 36%, rgba(185,188,191,0.9) 48%, var(--photo-deck) 100%),
      linear-gradient(90deg, var(--photo-pool), var(--photo-green));
  }
  .info-panel {
    position: absolute;
    left: 30px;
    top: 0;
    width: 470px;
    height: 400px;
    color: var(--white);
    text-align: center;
  }
  .brand-name {
    margin-top: 38px;
    font-family: "Montserrat", sans-serif;
    font-weight: 800;
    font-size: 64px;
    letter-spacing: 1px;
    text-transform: uppercase;
    line-height: 1;
  }
  .divider {
    height: 3px;
    background: var(--white);
    margin: 0 20px;
  }
  .divider.top { margin-top: 26px; }
  .tagline {
    font-family: "Montserrat", sans-serif;
    font-weight: 700;
    font-size: 38px;
    line-height: 1.12;
    text-transform: uppercase;
    margin: 14px 0 14px;
  }
  .contact-list {
    list-style: none;
    margin-top: 26px;
    padding-left: 70px;
    text-align: left;
    font-family: "Open Sans", sans-serif;
    font-weight: 700;
    font-size: 34px;
  }
  .contact-item {
    display: flex;
    align-items: center;
    gap: 16px;
    height: 48px;
  }
  .contact-icon { width: 30px; height: 30px; flex: none; }
</style>
</head>
<body>
  <div class="billboard">
    <svg class="billboard-shapes" width="1120" height="400" viewBox="0 0 1120 400" aria-hidden="true">
      <polygon points="0,0 85,0 0,80" fill="var(--red)"/>
      <polygon points="625,0 1120,0 1120,400 505,400" fill="var(--red)"/>
      <polygon points="530,0 640,0 560,265" fill="var(--red)"/>
    </svg>

    <div class="deck-photo" role="img" aria-label="Photo of a grey composite deck with black railings, two Adirondack chairs, a swimming pool and a fenced green backyard"></div>

    <div class="info-panel">
      <h1 class="brand-name">Plank QR</h1>
      <div class="divider top"></div>
      <p class="tagline">Outdoor Living<br>Spaces</p>
      <div class="divider"></div>
      <ul class="contact-list">
        <li class="contact-item">
          <svg class="contact-icon" viewBox="0 0 24 24" aria-hidden="true">
            <path fill="var(--red)" d="M6.6 10.8a15.1 15.1 0 0 0 6.6 6.6l2.2-2.2a1 1 0 0 1 1-.25 11.4 11.4 0 0 0 3.6.57 1 1 0 0 1 1 1V20a1 1 0 0 1-1 1A17 17 0 0 1 3 4a1 1 0 0 1 1-1h3.5a1 1 0 0 1 1 1c0 1.25.2 2.45.57 3.57a1 1 0 0 1-.25 1z"/>
            <path d="M14 3a7 7 0 0 1 7 7M14 6.5a3.5 3.5 0 0 1 3.5 3.5" stroke="var(--red)" stroke-width="2" fill="none" stroke-linecap="round"/>
          </svg>
          <span>416-283-9061</span>
        </li>
        <li class="contact-item">
          <svg class="contact-icon" viewBox="0 0 24 24" aria-hidden="true">
            <g fill="none" stroke="var(--red)" stroke-width="2">
              <circle cx="12" cy="12" r="9.5"/>
              <ellipse cx="12" cy="12" rx="4" ry="9.5"/>
              <path d="M2.5 12h19M4 7h16M4 17h16"/>
            </g>
          </svg>
          <span>www.plankqr.ca</span>
        </li>
      </ul>
    </div>
  </div>
</body>
</html>
```